Redesign of existing business card

I would like the "signage" attachment converted into a business card. This needs to be double sided aswell, keeping the phone number and names on the front, and the email + website on the back.

Second attachment is the current business card design.

Larger font for contact details is required.

Must keep to original color themes (electric blue, silver/grey etc)

Back of the card to have blue background with white writing.

Industry/Entity Type

Business

Contact Information for Business Card

Refer to existing design from attachments

Requirements
Must have
• Refer to existing design from attachments
Nice to have

```html
<!DOCTYPE html>
<html lang="en">
<head>
<meta charset="utf-8">
<title>Voltara Electrical Services – Business Card</title>
<link rel="stylesheet" href="https://fonts.googleapis.com/css2?family=Open+Sans:wght@700;800&display=swap">
<style>
  :root {
    --backdrop: #1e1e1f;
    --card: #ffffff;
    --electric-blue: #2f4fb0;
    --silver: #b3b7c0;
    --silver-light: #d9dce2;
    --white: #ffffff;
    --card-shadow: rgba(0, 0, 0, 0.55);
  }
  * { box-sizing: border-box; margin: 0; padding: 0; }
  html, body {
    width: 1200px;
    height: 1000px;
    overflow: hidden;
    background: var(--backdrop);
    font-family: "Open Sans", Arial, sans-serif;
  }
  .stage { position: relative; width: 1200px; height: 1000px; }
  .card {
    position: absolute;
    width: 580px;
    height: 330px;
    border-radius: 26px;
    box-shadow: 0 18px 40px var(--card-shadow);
    overflow: hidden;
  }
  .card--back { left: 150px; top: 150px; background: var(--electric-blue); }
  .card--front { left: 470px; top: 520px; background: var(--card); }

  .wordmark { line-height: 1; text-transform: uppercase; }
  .wordmark__name {
    display: block;
    font-size: 72px;
    font-weight: 800;
    letter-spacing: 2px;
    color: var(--silver);
  }
  .wordmark__tagline {
    display: block;
    font-size: 27px;
    font-weight: 800;
    letter-spacing: 2.5px;
    margin-top: 6px;
    color: var(--electric-blue);
  }

  .card--back .wordmark { position: absolute; left: 120px; top: 62px; }
  .card--back .wordmark__name { color: var(--silver-light); }
  .card--back .wordmark__tagline { color: var(--white); }
  .contact-lines {
    position: absolute;
    left: 0; right: 0; top: 222px;
    text-align: center;
    color: var(--white);
    font-weight: 700;
    font-size: 22px;
    line-height: 1.5;
  }

  .brand-row {
    position: absolute;
    left: 40px; top: 48px;
    display: flex;
    align-items: center;
    gap: 22px;
  }
  .brand-dot {
    width: 104px; height: 104px;
    border-radius: 50%;
    border: 8px solid var(--silver);
    flex: none;
  }
  .phone {
    position: absolute;
    right: 50px; bottom: 56px;
    display: flex;
    align-items: center;
    gap: 16px;
    color: var(--electric-blue);
    font-weight: 800;
    font-size: 50px;
    letter-spacing: 1px;
  }
  .phone__icon { width: 40px; height: 40px; fill: var(--electric-blue); }
</style>
</head>
<body>
<main class="stage">
  <section class="card card--back" aria-label="Card back">
    <div class="wordmark">
      <span class="wordmark__name">Voltara</span>
      <span class="wordmark__tagline">Electrical Services</span>
    </div>
    <div class="contact-lines">
      <p class="contact-lines__web">www.voltaraelectrical.com.au</p>
      <p class="contact-lines__email">hello@voltaraelectrical.com.au</p>
    </div>
  </section>

  <section class="card card--front" aria-label="Card front">
    <div class="brand-row">
      <span class="brand-dot" aria-hidden="true"></span>
      <div class="wordmark">
        <span class="wordmark__name">Voltara</span>
        <span class="wordmark__tagline">Electrical Services</span>
      </div>
    </div>
    <div class="phone">
      <svg class="phone__icon" viewBox="0 0 24 24" aria-hidden="true">
        <path d="M6.6 10.8a15.1 15.1 0 0 0 6.6 6.6l2.2-2.2a1 1 0 0 1 1-.25 11.4 11.4 0 0 0 3.6.57 1 1 0 0 1 1 1V20a1 1 0 0 1-1 1A17 17 0 0 1 3 4a1 1 0 0 1 1-1h3.5a1 1 0 0 1 1 1c0 1.25.2 2.45.57 3.57a1 1 0 0 1-.25 1z"/>
      </svg>
      <span class="phone__number">0400 555 123</span>
    </div>
  </section>
</main>
</body>
</html>
```